CORAL DRIFT INN GRAND OPENING

We are the new owners and just finished completely remodeling our property and rooms in January 2017. To attract new customers we are planning a HOTEL GRAND OPENING PARTY on FEBRUARY 16 , 2017. EVENT WILL START WITH A 5:00PM HAPPY HOUR
WE WILL HAVE: LIVE MUSIC, SNACKS & BOOZE
The event will be a LUAU PARTY THEME

Industry/Entity Type

Property

Font styles to use
Sans Serif

Colors
85cae6
3176b5
ee3036
cadf82
fbed22
fece3e

Requirements
Must have
• property address:
• 4927 Marlowe Lane
• Harlow Key, Fl 32814
• COMPANY LOGO

```html
<!DOCTYPE html>
<html lang="en">
<head>
<meta charset="utf-8">
<title>Coral Drift Inn – Hotel Grand Opening Party</title>
<link rel="stylesheet" href="https://fonts.googleapis.com/css2?family=Exo+2:wght@300;500;600;700;800&display=swap">
<style>
  :root {
    --sky: #85cae6;
    --ocean: #3176b5;
    --lime: #cadf82;
    --sun-yellow: #fbed22;
    --gold: #fece3e;
    --coral: #ee3036;
    --stone: #e2e2e2;
    --page: #f2f2f2;
    --white: #ffffff;
    --headline-white: #f4f4f4;
  }
  html, body {
    margin: 0;
    width: 1200px;
    height: 1040px;
    overflow: hidden;
    background: var(--page);
  }
  .flyer {
    position: absolute;
    left: 20px;
    top: 145px;
    width: 1160px;
    height: 751px;
    font-family: "Exo 2", sans-serif;
    box-shadow: 0 6px 10px rgba(0, 0, 0, 0.18);
  }
  .flyer svg { display: block; width: 100%; height: 100%; }
  .headline { font-weight: 800; fill: var(--headline-white); letter-spacing: 1.5px; }
  .headline-accent { fill: var(--sun-yellow); }
  .perk { font-weight: 700; fill: var(--ocean); font-size: 26px; }
  .note { font-weight: 700; fill: var(--lime); font-size: 21px; }
  .address { font-weight: 700; fill: var(--ocean); font-size: 17px; }
  .date-month { font-weight: 300; fill: var(--ocean); font-size: 53px; }
  .date-day { font-weight: 800; fill: var(--ocean); font-size: 53px; }
  .happy-label { font-weight: 700; fill: var(--ocean); font-size: 21px; }
  .happy-time { font-weight: 700; fill: var(--white); font-size: 32px; }
  .brand-name { font-weight: 600; fill: var(--ocean); font-size: 31px; letter-spacing: 1px; }
</style>
</head>
<body>
<div class="flyer">
  <svg viewBox="0 0 1244 805" xmlns="http://www.w3.org/2000/svg">
    <defs>
      <clipPath id="hero-clip">
        <polygon points="95,0 1244,0 1244,345 905,690 520,420"/>
      </clipPath>
      <linearGradient id="party-base" x1="0" y1="0" x2="1" y2="0.6">
        <stop offset="0" stop-color="#7fb2dc"/>
        <stop offset="0.22" stop-color="#b5654e"/>
        <stop offset="0.4" stop-color="#e9c98c"/>
        <stop offset="0.62" stop-color="#d9c7b2"/>
        <stop offset="0.82" stop-color="#b8c3d0"/>
        <stop offset="0.92" stop-color="#c24f64"/>
        <stop offset="1" stop-color="#7ea8d2"/>
      </linearGradient>
      <radialGradient id="sun-glow" cx="0.63" cy="0.36" r="0.42">
        <stop offset="0" stop-color="#fffbe8" stop-opacity="1"/>
        <stop offset="0.3" stop-color="#fbe3a0" stop-opacity="0.85"/>
        <stop offset="0.7" stop-color="#f0b866" stop-opacity="0.25"/>
        <stop offset="1" stop-color="#f0b866" stop-opacity="0"/>
      </radialGradient>
      <linearGradient id="sea-haze" x1="0" y1="0" x2="0" y2="1">
        <stop offset="0.55" stop-color="#5f8fb6" stop-opacity="0"/>
        <stop offset="1" stop-color="#4d7ea8" stop-opacity="0.55"/>
      </linearGradient>
      <linearGradient id="living-room" x1="0" y1="0" x2="0" y2="1">
        <stop offset="0" stop-color="#f2f4f3"/>
        <stop offset="0.55" stop-color="#cfd3d4"/>
        <stop offset="0.75" stop-color="#8a8f96"/>
        <stop offset="1" stop-color="#b59772"/>
      </linearGradient>
      <linearGradient id="bedroom" x1="0" y1="0" x2="0" y2="1">
        <stop offset="0" stop-color="#eceeed"/>
        <stop offset="0.5" stop-color="#d6d2c8"/>
        <stop offset="0.8" stop-color="#f4f3ef"/>
        <stop offset="1" stop-color="#c9c6bd"/>
      </linearGradient>
      <linearGradient id="team-lawn" x1="0" y1="0" x2="0" y2="1">
        <stop offset="0" stop-color="#5f9bd0"/>
        <stop offset="0.35" stop-color="#3f7a4a"/>
        <stop offset="0.55" stop-color="#f3f4f4"/>
        <stop offset="0.78" stop-color="#e8e9ea"/>
        <stop offset="1" stop-color="#6e9a45"/>
      </linearGradient>
    </defs>

    <!-- base -->
    <rect class="base" width="1244" height="805" fill="var(--stone)"/>

    <!-- hero photo area -->
    <g class="hero-photo" role="img" aria-label="Photo of friends dancing on the beach at sunset, luau party mood" clip-path="url(#hero-clip)">
      <rect width="1244" height="805" fill="url(#party-base)"/>
      <rect width="1244" height="805" fill="url(#sun-glow)"/>
      <rect width="1244" height="805" fill="url(#sea-haze)"/>
    </g>

    <!-- white accent band on the right -->
    <polygon class="accent-band" points="1244,345 1244,372 895,712 868,700" fill="var(--white)"/>

    <!-- blue panel -->
    <polygon class="blue-panel" points="0,0 95,0 520,420 80,805 0,805" fill="var(--ocean)"/>

    <!-- white diagonal stripe -->
    <polygon class="stripe" points="95,0 128,0 372,222 339,222" fill="var(--white)"/>

    <!-- small lime diamond -->
    <polygon class="badge-diamond" points="150,41 199,90 150,139 101,90" fill="var(--lime)"/>

    <!-- happy hour diamond -->
    <g class="happy-hour">
      <polygon points="268,45 356,133 268,221 180,133" fill="var(--lime)"/>
      <text class="happy-label" x="266" y="124" text-anchor="middle">Happy Hour</text>
      <text class="happy-time" x="268" y="153" text-anchor="middle">5.00 pm</text>
    </g>

    <!-- photo diamonds -->
    <polygon class="room-photo" role="img" aria-label="Photo of a renovated living room"
      points="467,175 609,317 467,459 325,317" fill="url(#living-room)" stroke="var(--lime)" stroke-width="6"/>
    <polygon class="room-photo" role="img" aria-label="Photo of a renovated bedroom"
      points="622,325 764,467 622,609 480,467" fill="url(#bedroom)" stroke="var(--lime)" stroke-width="6"/>
    <polygon class="team-photo" role="img" aria-label="Photo of the hotel staff holding a banner on the lawn"
      points="779,480 921,622 779,764 637,622" fill="url(#team-lawn)" stroke="var(--lime)" stroke-width="6"/>

    <!-- headline -->
    <g class="headline">
      <text x="22" y="300" font-size="74">HOTEL</text>
      <text x="22" y="365" font-size="72">GRAND</text>
      <text x="22" y="417" font-size="60">OPENING</text>
      <text class="headline-accent" x="22" y="482" font-size="74">PARTY</text>
    </g>

    <!-- perks bar -->
    <g class="perks">
      <polygon points="26,527 26,522 40,510 52,510 64,527" fill="var(--sun-yellow)"/>
      <rect x="26" y="527" width="491" height="35" fill="var(--sun-yellow)"/>
      <text class="perk" x="48" y="554">Live Music</text>
      <rect x="191" y="534" width="2" height="22" fill="var(--ocean)"/>
      <text class="perk" x="214" y="554">Snacks &amp; Booze</text>
    </g>

    <!-- renovation note -->
    <g class="note">
      <text x="27" y="602">PROPERTY HAS RECENTLY</text>
      <text x="27" y="628">BEEN COMPLETELY</text>
      <text x="27" y="655">RENOVATED</text>
    </g>

    <!-- location -->
    <g class="location">
      <polygon points="167,668 209,710 167,752 125,710" fill="var(--sky)"/>
      <path d="M167,694 a12,12 0 0 1 12,12 c0,9 -12,22 -12,22 c0,0 -12,-13 -12,-22 a12,12 0 0 1 12,-12 z" fill="var(--white)"/>
      <circle cx="167" cy="706" r="4.5" fill="var(--sky)"/>
      <text class="address" x="247" y="707">CORAL DRIFT INN</text>
      <text class="address" x="247" y="729">4927 MARLOWE LANE</text>
      <text class="address" x="247" y="751">HARLOW KEY, FL 32814</text>
    </g>

    <!-- date -->
    <g class="date">
      <rect x="505" y="694" width="2" height="60" fill="var(--ocean)"/>
      <text x="518" y="753"><tspan class="date-month">Feb</tspan><tspan class="date-day">16</tspan></text>
    </g>

    <!-- brand -->
    <g class="brand">
      <circle cx="1096" cy="640" r="24" fill="var(--gold)"/>
      <text class="brand-name" x="1096" y="738" text-anchor="middle">CORAL DRIFT INN</text>
    </g>
  </svg>
</div>
</body>
</html>
```